Business cards for KORBEN Real Estate Properties LLC

We need a cool, original business card design for a company based in the Washington DC metropolitan area. We are a new energetic and passionate Real Estate Investing Company that invests in all types of real estate; commercial, residential, industrial etc.

Our company color is Red since it reflects action, energy and speed; it is assertive confident, energizing, exciting, powerful, passionate and determined. So we would like business card communicate those qualities to the audience.

Our audiences are investors that want to invest with us, real estate sellers, buyers, and tenants who lease from us.

Our logo is attached

```html
<!DOCTYPE html>
<html lang="en">
<head>
<meta charset="utf-8">
<title>KORBEN Real Estate Properties LLC — Business Cards</title>
<link rel="stylesheet" href="https://fonts.googleapis.com/css2?family=Orbitron:wght@700;900&family=Encode+Sans+Condensed:wght@400;500&family=PT+Serif&display=swap">
<style>
  :root {
    --brand-red: #c8202a;
    --ink: #111111;
    --steel: #a9aaac;
    --steel-light: #c9cacc;
    --paper: #ffffff;
    --backdrop: #f2f2f2;
    --card-shadow: rgba(0, 0, 0, 0.18);
  }

  * { box-sizing: border-box; margin: 0; padding: 0; }

  html, body {
    width: 1200px;
    height: 873px;
    overflow: hidden;
    background: var(--backdrop);
  }

  .canvas {
    position: relative;
    width: 1200px;
    height: 873px;
    display: flex;
    align-items: center;
    justify-content: center;
    gap: 48px;
  }

  .card {
    position: relative;
    width: 520px;
    height: 297px;
    background: var(--paper);
    box-shadow: 0 10px 28px var(--card-shadow);
    overflow: hidden;
  }

  /* ---------- Front ---------- */
  .card-front .brand {
    position: absolute;
    left: 34px;
    top: 40px;
    display: flex;
    align-items: center;
    gap: 18px;
  }

  .brand-dot {
    width: 58px;
    height: 58px;
    border-radius: 50%;
    background: var(--brand-red);
  }

  .brand-name {
    font-family: "Orbitron", sans-serif;
    font-weight: 900;
    font-size: 64px;
    letter-spacing: 2px;
    line-height: 1;
    color: var(--ink);
  }

  .tagline {
    position: absolute;
    left: 110px;
    top: 116px;
    font-family: "Encode Sans Condensed", sans-serif;
    font-weight: 500;
    font-size: 19px;
    letter-spacing: 0.5px;
    color: var(--ink);
    text-transform: uppercase;
  }

  .contact {
    position: absolute;
    left: 110px;
    top: 168px;
    display: grid;
    grid-template-columns: auto auto;
    column-gap: 14px;
    row-gap: 8px;
    align-items: baseline;
  }

  .contact-label {
    font-family: "Orbitron", sans-serif;
    font-weight: 700;
    font-size: 13px;
    color: var(--brand-red);
    text-transform: uppercase;
    text-align: right;
  }

  .contact-value {
    font-family: "PT Serif", serif;
    font-size: 17px;
    color: var(--ink);
  }

  /* ---------- Back ---------- */
  .card-back .lower-band {
    position: absolute;
    left: 0;
    right: 0;
    bottom: 0;
    height: 42%;
    background: linear-gradient(180deg, var(--steel-light), var(--steel));
  }

  .card-back .brand {
    position: absolute;
    inset: 0;
    display: flex;
    align-items: center;
    justify-content: center;
    padding-bottom: 40px;
  }

  .card-back .brand-name {
    color: var(--brand-red);
    font-size: 78px;
    letter-spacing: 4px;
  }
</style>
</head>
<body>
  <main class="canvas">
    <section class="card card-front" aria-label="Business card front">
      <div class="brand">
        <span class="brand-dot" aria-hidden="true"></span>
        <span class="brand-name">KORBEN</span>
      </div>
      <p class="tagline">Real Estate Properties LLC</p>
      <dl class="contact">
        <dt class="contact-label">Phone:</dt>
        <dd class="contact-value">202-555-0147</dd>
        <dt class="contact-label">Web:</dt>
        <dd class="contact-value">korbenprop.com</dd>
        <dt class="contact-label">Email:</dt>
        <dd class="contact-value">j.carter@korbenprop.com</dd>
      </dl>
    </section>

    <section class="card card-back" aria-label="Business card back">
      <div class="lower-band" aria-hidden="true"></div>
      <div class="brand">
        <span class="brand-name">KORBEN</span>
      </div>
    </section>
  </main>
</body>
</html>
```